April 11th Event- Islamorada- Coaching/Tarot/Hypnotherapy

Hi! Need a flyer that can also be posted on social media. Directions attached. Also will need a version that 2 can fit on 1 piece of paper so I can cut in half for hand outs. PDF example attached as well so you can understand. Thank you!

AAAAAAAAAAAAAAAAAAAAAAAAAAAAAAAAAAAAAAAAAAAAAAAAAAAAAAAAAAAAAAAAAAAAAAAAAAAAAAAAAAAAAAAAAAAAAAAAAAAAAAAAAAAAAAAAAAAAAAAAAAAAAAAAAAAAAAAAAAAAAAAAAAAAAAAAAAAAAAAAAAAAAAAAAAAAAAAAAAAAAAAAAAAAAAAAAAAAAAAAAAAAAAAAAAAAAAAAAAAAAAAAAA

Target Market(s)

Female audience age 35-70.
Spiritual, sophisticated

Industry/Entity Type

Event Planning

Font styles to use
Serif

Colors
d2a4cc
3176b5
85acd3
b868aa
e667a6
eea4c8
f59296
fbf289
add136

Requirements
Must have
• See attachments
Nice to have
• See attachments

```html
<!DOCTYPE html>
<html lang="en">
<head>
<meta charset="utf-8">
<title>Get the 411 – Evening of Self Discovery</title>
<link rel="stylesheet" href="https://fonts.googleapis.com/css2?family=Gelasio:wght@400;700&family=Parisienne&display=swap">
<style>
  :root {
    --blue: #3176b5;
    --orchid: #b868aa;
    --lavender: #d2a4cc;
    --rose: #eea4c8;
    --coral: #f59296;
    --paper: #eeedee;
    --page: #ffffff;
  }
  * { margin: 0; padding: 0; box-sizing: border-box; }
  html, body { width: 1200px; height: 1200px; overflow: hidden; background: var(--page); }
  .flyer {
    position: absolute; left: 240px; top: 44px; width: 720px; height: 1112px;
    background: var(--paper); overflow: hidden;
    font-family: "Gelasio", Georgia, serif;
  }
  .decor { position: absolute; inset: 0; }
  .line { position: absolute; white-space: nowrap; line-height: 1; }
  .center { left: 0; width: 760px; text-align: center; }
  .headline { font-family: "Parisienne", cursive; color: var(--orchid); font-size: 64px; }
  .invite { color: var(--orchid); font-size: 25px; }
  .date { color: var(--blue); font-weight: 700; font-size: 62px; }
  .doors { color: var(--blue); font-size: 26px; }
  .time { color: var(--orchid); font-weight: 700; font-size: 38px; }
  .venue { color: var(--blue); font-weight: 700; font-size: 34px; }
  .directions { color: var(--blue); font-size: 23px; }
  .speakers-label { left: 10px; top: 652px; color: var(--blue); font-weight: 700; font-size: 21px; }
  .speaker { position: absolute; top: 688px; width: 240px; }
  .speaker-name { color: var(--blue); font-weight: 700; font-size: 21px; line-height: 1.2; }
  .speaker-role { color: var(--orchid); font-size: 18px; line-height: 24px; white-space: nowrap; }
  .tickets { color: var(--blue); font-weight: 700; font-size: 38px; }
  .drinks { color: var(--blue); font-size: 27px; }
  .note { color: var(--orchid); font-size: 22px; }
  .contact-line { color: var(--orchid); font-size: 28px; }
  .contact { color: var(--blue); font-weight: 700; font-size: 32px; }
</style>
</head>
<body>
<div class="flyer">
  <svg class="decor" width="720" height="1112" viewBox="0 0 720 1112">
    <defs>
      <linearGradient id="stroke" x1="0" y1="1" x2="1" y2="0">
        <stop offset="0" stop-color="#d2a4cc" stop-opacity="0.25"/>
        <stop offset="1" stop-color="#d2a4cc" stop-opacity="0.55"/>
      </linearGradient>
      <radialGradient id="bloom" cx="0.5" cy="0.5" r="0.5">
        <stop offset="0" stop-color="#eea4c8"/>
        <stop offset="1" stop-color="#f6d8e6"/>
      </radialGradient>
    </defs>
    <g role="img" aria-label="Painted lavender brush stroke sweeping diagonally across the page">
      <polygon points="40,1000 150,990 720,240 720,150 660,150" fill="url(#stroke)"/>
    </g>
    <g role="img" aria-label="Cluster of pink and lavender roses with green leaves">
      <ellipse cx="90" cy="70" rx="120" ry="100" fill="url(#bloom)" opacity="0.8"/>
      <ellipse cx="290" cy="90" rx="130" ry="110" fill="url(#bloom)" opacity="0.75"/>
      <ellipse cx="160" cy="250" rx="110" ry="70" fill="#b7c9a8" opacity="0.45"/>
      <ellipse cx="165" cy="270" rx="45" ry="40" fill="#d2c4dc" opacity="0.8"/>
      <ellipse cx="60" cy="330" rx="55" ry="45" fill="#d2c4dc" opacity="0.6"/>
    </g>
    <g role="img" aria-label="Coral pink rose at left edge">
      <ellipse cx="40" cy="460" rx="95" ry="105" fill="#f59296" opacity="0.55"/>
    </g>
    <g role="img" aria-label="Roses and leaves in the bottom right corner">
      <ellipse cx="710" cy="800" rx="24" ry="60" fill="#f59296" opacity="0.55"/>
      <ellipse cx="660" cy="980" rx="80" ry="110" fill="#9fb595" opacity="0.45"/>
      <ellipse cx="670" cy="1060" rx="60" ry="40" fill="#d2c4dc" opacity="0.8"/>
      <ellipse cx="530" cy="1100" rx="90" ry="40" fill="url(#bloom)" opacity="0.7"/>
    </g>
    <path id="tagline-arc" d="M48,108 Q400,330 716,88" fill="none"/>
    <text font-family="Parisienne, cursive" font-size="33" fill="#b868aa">
      <textPath href="#tagline-arc" textLength="690" lengthAdjust="spacingAndGlyphs">Open Yourself Up To The Info You Have Inside</textPath>
    </text>
  </svg>

  <div class="line center headline" style="top:74px">Get the 411</div>
  <div class="line center invite" style="top:262px">Please Join Us For An Evening of</div>
  <div class="line center invite" style="top:296px">Self Discovery, Enlightment and Fun!</div>
  <div class="line center date" style="top:346px">Thursday April 11th</div>
  <div class="line center doors" style="top:418px">Doors Open at 5:30</div>
  <div class="line center time" style="top:460px">Event from 6pm-8pm</div>
  <div class="line center venue" style="top:514px">The Gardens at Miss Marlowe</div>
  <div class="line center venue" style="top:558px">80940 Overseas Highway Islamorada</div>
  <div class="line center directions" style="top:594px">(MM81 Bayside behind Harbor Market)</div>

  <div class="line speakers-label">Speakers:</div>
  <div class="speaker" style="left:10px">
    <div class="speaker-name">Marina Holloway</div>
    <div class="speaker-role">The Kind Path Life<br>Coach<br>Certified Professional Life<br>Coach</div>
  </div>
  <div class="speaker" style="left:262px">
    <div class="speaker-name">Celia Brandt</div>
    <div class="speaker-role">Licensed Hypnotherapist<br>Wonder Holistic<br>Gifts &amp; Therapies</div>
  </div>
  <div class="speaker" style="left:512px">
    <div class="speaker-name">Joan Sterling</div>
    <div class="speaker-role">Tarot Readings/EM Path<br>Spiritual Counselor</div>
  </div>

  <div class="line center tickets" style="top:862px">Tickets $15 each</div>
  <div class="line center drinks" style="top:910px">(Drinks included)</div>
  <div class="line center note" style="top:952px">Names must be on the guest list</div>
  <div class="line center contact-line" style="top:982px">For tickets contact Marina Holloway</div>
  <div class="line center contact" style="top:1020px">Marina@thekindpathlifecoach.com</div>
  <div class="line center contact" style="top:1060px">305-555-0142</div>
</div>
</body>
</html>
```